Upmarket Bathroom and Kitchen ware supplier needs a classy business card design

We are a company based in Fiji, we sell plumbing ware (Kitchen and bathroom taps, Basins,showers, toilets etc) through up market show rooms to individuals and directly through Architects and designers of resorts and holiday houses for new builds and renovations. we are wanting to upgrade our over all look and brand. we are starting with a new logo but will be rebranding the whole business. This project is for a business card design for my management and tales team I would like it to be dark, classy and interesting

Target Market(s)

Resort directors and Management, High end holiday home owners

Contact Information for Business Card

Neil Dawson
Director
+64219473815

Colors

Designer to choose colors to be used in the design.

Requirements
Must have
• Must have an upmarket appearance I like darker charcoal shades but will be guided by the designers
• Please any catch phrases like "Crafting remarkable living rooms" this belongs tpo one of our suppliers so can not be used.
Nice to have
• Double sided, so front dedicated to logo provided and back info about the business and the person.

```html
<!DOCTYPE html>
<html lang="en">
<head>
<meta charset="utf-8">
<title>Serene Interiors – Business Card</title>
<link href="https://fonts.googleapis.com/css2?family=Josefin+Sans:wght@300&family=Oswald:wght@400;500&display=swap" rel="stylesheet">
<style>
  :root {
    --backdrop: #a19f98;
    --charcoal: #2b2a2a;
    --stone: #c9c5be;
    --ash: #a8a6a1;
    --line: #8e8b86;
  }
  html, body {
    margin: 0;
    padding: 0;
    width: 1200px;
    height: 960px;
    overflow: hidden;
    background: var(--backdrop);
  }
  .card {
    position: absolute;
    width: 505px;
    height: 289px;
    background: var(--charcoal);
    overflow: hidden;
  }
  .card svg { display: block; width: 100%; height: 100%; }
  .card--front { left: 78px; top: 332px; }
  .card--back { left: 611px; top: 333px; }
  .brand-name {
    font-family: "Josefin Sans", sans-serif;
    font-weight: 300;
    fill: var(--stone);
  }
  .contact-name, .contact-role, .contact-phone {
    font-family: "Oswald", sans-serif;
    fill: var(--ash);
  }
</style>
</head>
<body>

<section class="card card--front" aria-label="Card front">
  <svg viewBox="0 0 906 518" preserveAspectRatio="none">
    <defs>
      <radialGradient id="ornament-left-front" cx="0" cy="0.5" r="1">
        <stop offset="0" stop-color="#55534f"/>
        <stop offset="1" stop-color="#2b2a2a"/>
      </radialGradient>
      <radialGradient id="ornament-corner-front" cx="1" cy="1" r="1">
        <stop offset="0" stop-color="#55534f"/>
        <stop offset="1" stop-color="#2b2a2a"/>
      </radialGradient>
    </defs>
    <rect class="ornament ornament--left" x="0" y="15" width="145" height="405" fill="url(#ornament-left-front)" role="img" aria-label="Decorative concentric arc ornament on the left edge"/>
    <rect class="ornament ornament--corner" x="720" y="340" width="186" height="178" fill="url(#ornament-corner-front)" role="img" aria-label="Decorative concentric arc ornament in the lower right corner"/>
    <g class="brand">
      <circle cx="453" cy="225" r="52" fill="none" stroke="var(--stone)" stroke-width="5"/>
      <text class="brand-name" x="453" y="345" text-anchor="middle" font-size="34" letter-spacing="9">SERENE INTERIORS</text>
    </g>
  </svg>
</section>

<section class="card card--back" aria-label="Card back">
  <svg viewBox="0 0 906 518" preserveAspectRatio="none">
    <defs>
      <radialGradient id="ornament-left-back" cx="0" cy="0.5" r="1">
        <stop offset="0" stop-color="#55534f"/>
        <stop offset="1" stop-color="#2b2a2a"/>
      </radialGradient>
    </defs>
    <rect class="ornament ornament--left" x="0" y="15" width="145" height="405" fill="url(#ornament-left-back)" role="img" aria-label="Decorative concentric arc ornament on the left edge"/>
    <g class="contact">
      <text class="contact-name" x="632" y="418" text-anchor="end" font-size="27" font-weight="500" letter-spacing="3">NEIL DAWSON</text>
      <text class="contact-role" x="632" y="451" text-anchor="end" font-size="18" letter-spacing="2.5">DIRECTOR</text>
      <line class="contact-divider" x1="652" y1="392" x2="652" y2="455" stroke="var(--line)" stroke-width="1.5"/>
      <g class="icon-phone" fill="none" stroke="var(--ash)" stroke-width="2">
        <rect x="674" y="430" width="10" height="17" rx="1.5"/>
        <line x1="677" y1="444" x2="681" y2="444"/>
      </g>
      <text class="contact-phone" x="702" y="451" font-size="18" letter-spacing="3">64219473815</text>
    </g>
  </svg>
</section>

</body>
</html>
```